Monument sign* - Law Firm

*I am installing a monument sign that has LED, as well as backlit elements. I am seeking help in designing the backlit portion of the sign. The Backlit sign will be 12’ x 4’.

We are looking for a classic, yet eye-catching sign to help new and current clients find our firm as well as bring in future clients. One of our goals is that people who drive by on a regular basis remember our sign (and us) for any future legal need.

Target Market(s)

Current and future clientele

Industry/Entity Type

Law Firm

Font styles to use
Serif
Sans Serif

Colors
b1b1b1
333333

Requirements
Must have
• Business name: Hargrove Law Firm, Inc.
• Website: www.hargrovelawfirm-example.com
• Telephone: (555)214-3679
• Our firm's logo
Nice to have
• Color preference is black, taupe, and white. A photo for reference of the office coloring is uploaded.
• We currently have an established logo which our firm has been using for more than 10 years. Our logo has been used in advertising, commercials, letterhead, and on-site. We are looking to transition from brown/rust/cream to the black/taupe/white color scheme.
Should not have
• Cheesy slogans; character designs; directions; additional symbols outside of the firm's logo.

```html
<!DOCTYPE html>
<html lang="en">
<head>
<meta charset="utf-8">
<title>Hargrove Law Firm, Inc. — Monument Sign</title>
<link rel="stylesheet" href="https://fonts.googleapis.com/css2?family=Bebas+Neue&family=Arimo:wght@400&display=swap">
<style>
  :root {
    --page: #ffffff;
    --panel: #1e1e1d;
    --photo-dark: #2a2a2a;
    --photo-mid: #4a4a4a;
    --photo-light: #6e6e6e;
    --brand: #c07a3e;
    --white: #ffffff;
  }
  html, body {
    margin: 0;
    padding: 0;
    overflow: hidden;
    background: var(--page);
  }
  .canvas {
    position: relative;
    width: 1200px;
    height: 480px;
    background: var(--page);
    overflow: hidden;
  }
  .sign {
    position: absolute;
    left: 120px;
    top: 80px;
    width: 960px;
    height: 320px;
    background: var(--page);
  }
  .brand-panel {
    position: absolute;
    left: 0;
    top: 0;
    width: 284px;
    height: 320px;
    background: var(--panel);
  }
  .logo-block {
    position: absolute;
    left: 82px;
    top: 78px;
    width: 132px;
    height: 141px;
    display: flex;
    flex-direction: column;
    align-items: center;
    justify-content: center;
    gap: 12px;
  }
  .logo-square {
    width: 64px;
    height: 64px;
    background: var(--brand);
  }
  .logo-name {
    font-family: "Bebas Neue", sans-serif;
    font-size: 26px;
    line-height: 1;
    color: var(--white);
    text-align: center;
    letter-spacing: 1px;
  }
  .phone {
    position: absolute;
    left: 50px;
    top: 262px;
    display: flex;
    align-items: center;
    gap: 6px;
    font-family: "Arimo", sans-serif;
    font-size: 23px;
    color: var(--white);
    text-shadow: 0 2px 4px rgba(0,0,0,0.6);
  }
  .phone-icon {
    width: 24px;
    height: 24px;
  }
  .photo-panel {
    position: absolute;
    left: 288px;
    top: 0;
    width: 672px;
    height: 320px;
    overflow: hidden;
  }
  .photo-backdrop {
    position: absolute;
    inset: 0;
    background: linear-gradient(160deg, var(--photo-dark) 0%, var(--photo-light) 35%, var(--photo-mid) 60%, var(--photo-dark) 100%);
  }
  .firm-name {
    position: absolute;
    left: 0;
    right: 0;
    top: 106px;
    margin: 0;
    text-align: center;
    font-family: "Bebas Neue", sans-serif;
    font-weight: 400;
    font-size: 70px;
    line-height: 1;
    color: var(--white);
    text-shadow: 3px 4px 6px rgba(0,0,0,0.7);
  }
  .website {
    position: absolute;
    right: 42px;
    top: 266px;
    font-family: "Arimo", sans-serif;
    font-size: 22px;
    color: var(--white);
    text-shadow: 0 2px 4px rgba(0,0,0,0.6);
  }
</style>
</head>
<body>
<div class="canvas">
  <div class="sign">
    <section class="brand-panel">
      <div class="logo-block">
        <div class="logo-square"></div>
        <div class="logo-name">Hargrove Law Firm</div>
      </div>
      <div class="phone">
        <svg class="phone-icon" viewBox="0 0 24 24" aria-hidden="true">
          <circle cx="12" cy="12" r="10.5" fill="none" stroke="#ffffff" stroke-width="1.6"/>
          <path d="M9.2 6.5c-1 .4-1.6 1.3-1.6 2.6 0 3 2.4 7.4 5 8.6 1 .5 2.1.2 2.8-.6l-1.8-2.2-1.2.6c-1-.7-2-2.7-2.1-3.9l1.2-.5-.6-2.8z" fill="#ffffff"/>
        </svg>
        <span>(555)214-3679</span>
      </div>
    </section>
    <section class="photo-panel">
      <div class="photo-backdrop" role="img" aria-label="Black and white photograph of a classical courthouse facade with columns and a dome"></div>
      <h1 class="firm-name">Hargrove Law Firm, Inc.</h1>
      <div class="website">www.hargrovelawfirm-example.com</div>
    </section>
  </div>
</div>
</body>
</html>
```